New Design required for Disposable Gloves Pack

We need a new design for our range of disposable Gloves.
The brand name is "Marlow" I will attach the existing logo.

The needs to be 3 variations of the design (maybe different colours) that we can use for the different kinds of gloves: Latex Gloves, Clear Vinyl Gloves & Blue Vinyl Gloves.
Pack size is: 220x65x120mm.

Attached is a template to use showing all sides of the pack as flat. It is preferable that you supply an image of the complete folded pack as well with your design. Also attached is a PDF of our old pack design. Please use all the text on this old design for the new one.

The packs need to be easily differentiated from each other.

Target Market(s)

New Zealand Businesses, food processors & manufacturers. Medical & health care professionals

Font styles to use
Sans Serif

Requirements
Must have
• 3 variations of the same pack design to differentiate between the 3 types of gloves we offer: Latex Gloves, Clear Vinyl & Blue Vinyl Gloves.

```html
<!DOCTYPE html>
<html lang="en">
<head>
<meta charset="utf-8">
<title>Marlow Blue Vinyl Gloves – Pack Dieline</title>
<link href="https://fonts.googleapis.com/css2?family=Raleway:wght@300;400;700&family=Tinos&display=swap" rel="stylesheet">
<style>
  :root {
    --navy: #263d68;
    --teal: #0099bb;
    --green: #78b800;
    --white: #ffffff;
    --ink: #111111;
    --outline: #222222;
    --sans: "Raleway", Arial, sans-serif;
    --serif: "Tinos", "Times New Roman", serif;
  }
  html, body {
    margin: 0;
    padding: 0;
    width: 1200px;
    height: 1200px;
    overflow: hidden;
    background: var(--white);
  }
  .dieline { display: block; width: 1200px; height: 1200px; }
  .spec-label { font-family: var(--serif); font-size: 23px; fill: var(--ink); }
  .fill-navy { fill: var(--navy); }
  .fill-teal { fill: var(--teal); }
  .fill-white { fill: var(--white); }
  .fill-green { fill: var(--green); }
  .panel-edge { fill: none; stroke: var(--outline); stroke-width: 1.2; }
  .dispenser-cut { fill: none; stroke: var(--white); stroke-width: 1.4; stroke-dasharray: 5 4; }
  .title { font-family: var(--sans); font-weight: 300; }
  .title .bold { font-weight: 700; }
  .title-light { fill: var(--white); }
  .title-accent { fill: var(--teal); }
  .title-navy { fill: var(--navy); }
  .title-green { fill: var(--green); }
  .brand-name { font-family: var(--sans); font-weight: 400; letter-spacing: 4px; }
  .size-tag { font-family: var(--sans); font-weight: 700; font-size: 15px; letter-spacing: 5px; fill: var(--white); }
  .size-rule { stroke: var(--white); stroke-width: 1.5; }
  .band-text { font-family: var(--sans); font-weight: 400; font-size: 15px; fill: var(--white); }
  .side-info { font-family: var(--sans); font-weight: 400; font-size: 15px; fill: var(--green); }
  .glove-art { fill: var(--teal); }
</style>
</head>
<body>
<svg class="dieline" viewBox="0 0 1500 1500" xmlns="http://www.w3.org/2000/svg">

  <!-- Pack specification -->
  <text class="spec-label" x="21" y="381">PACK SIZE</text>
  <text class="spec-label" x="21" y="411">220 x 65 x 120mm</text>

  <!-- Top panel -->
  <g class="panel-top">
    <rect class="fill-navy" x="390" y="253" width="718" height="391"/>
    <path class="fill-teal" d="M390,437 C470,437 530,480 580,520 C640,570 720,582 800,557 C900,522 980,478 1108,492 L1108,644 L390,644 Z"/>
    <path class="fill-white" d="M390,453 C470,455 520,495 570,535 C640,588 720,592 810,568 C900,540 990,500 1108,514 L1108,644 L390,644 Z"/>
    <rect class="dispenser-cut" x="560" y="401" width="380" height="96" rx="26"/>
    <text class="title" x="1086" y="303" font-size="40" text-anchor="end"><tspan class="title-light">BLUE VINLY </tspan><tspan class="bold title-accent">GLOVES</tspan></text>
    <rect class="glove-art" x="400" y="510" width="185" height="130" rx="18" role="img" aria-label="Illustration of a pair of blue gloves"/>
    <text class="brand-name fill-green" x="1088" y="625" font-size="48" text-anchor="end">MARLOW</text>
    <rect class="panel-edge" x="390" y="253" width="718" height="391"/>
  </g>

  <!-- Front panel -->
  <g class="panel-front">
    <rect class="fill-white" x="390" y="644" width="718" height="190"/>
    <path class="fill-teal" d="M390,740 C500,762 600,725 700,690 C780,668 850,668 920,705 C990,750 1040,785 1108,787 L1108,834 L390,834 Z"/>
    <path class="fill-navy" d="M390,755 C500,778 600,742 700,708 C780,684 850,684 915,722 C985,768 1040,800 1108,803 L1108,834 L390,834 Z"/>
    <text class="title title-navy" x="407" y="695" font-size="27"><tspan>BLUE VINLY </tspan><tspan class="bold">GLOVES</tspan></text>
    <text class="brand-name fill-green" x="1085" y="708" font-size="25" text-anchor="end" letter-spacing="2">MARLOW</text>
    <text class="size-tag" x="419" y="803">LARGE</text>
    <line class="size-rule" x1="392" y1="810" x2="498" y2="810"/>
    <rect class="fill-white" x="476" y="808" width="22" height="6"/>
    <rect class="glove-art" x="725" y="705" width="185" height="129" rx="18" role="img" aria-label="Illustration of a pair of blue gloves"/>
    <rect class="fill-green" x="390" y="834" width="718" height="21"/>
    <text class="band-text" x="750" y="851" text-anchor="middle">Ambidexterous . Single use . Lightly Powered</text>
    <rect class="panel-edge" x="390" y="644" width="718" height="211"/>
  </g>

  <!-- Left side panel -->
  <g class="panel-side">
    <rect class="fill-white" x="0" y="644" width="390" height="190"/>
    <text class="title title-green" x="82" y="750" font-size="23"><tspan class="bold">BLUE</tspan><tspan> VINLY GLOVES</tspan></text>
    <text class="side-info" x="16" y="801">Reoder Code</text>
    <text class="side-info" x="16" y="822">######</text>
    <rect class="fill-green" x="0" y="834" width="390" height="21"/>
    <text class="band-text" x="14" y="850">www.harbourpak.co.nz</text>
    <text class="band-text" x="248" y="852">0800 410 336</text>
    <rect class="panel-edge" x="0" y="644" width="390" height="211"/>
  </g>

  <!-- Right side panel -->
  <g class="panel-side">
    <rect class="fill-white" x="1108" y="644" width="392" height="190"/>
    <text class="title title-green" x="1187" y="750" font-size="23"><tspan class="bold">BLUE</tspan><tspan> VINLY GLOVES</tspan></text>
    <text class="side-info" x="1121" y="801">Reoder Code</text>
    <text class="side-info" x="1121" y="822">######</text>
    <rect class="fill-green" x="1108" y="834" width="392" height="21"/>
    <text class="band-text" x="1120" y="850">www.harbourpak.co.nz</text>
    <text class="band-text" x="1355" y="852">0800 410 336</text>
    <rect class="panel-edge" x="1108" y="644" width="391" height="211"/>
  </g>

  <!-- Bottom / back panel -->
  <g class="panel-back">
    <rect class="fill-navy" x="390" y="855" width="718" height="391"/>
    <text class="size-tag" x="524" y="940">LARGE</text>
    <line class="size-rule" x1="496" y1="946" x2="604" y2="946"/>
    <rect class="fill-white" x="580" y="944" width="24" height="6"/>
    <text class="title" x="770" y="1068" font-size="40" text-anchor="middle"><tspan class="title-light">BLUE VINLY </tspan><tspan class="bold title-accent">GLOVES</tspan></text>
    <rect class="glove-art" x="415" y="1115" width="185" height="131" rx="18" role="img" aria-label="Illustration of a pair of blue gloves"/>
    <text class="brand-name fill-white" x="1083" y="1228" font-size="52" text-anchor="end">MARLOW</text>
    <rect class="panel-edge" x="390" y="855" width="718" height="391"/>
  </g>

</svg>
</body>
</html>
```